Online Marketplace Startup for Community Facilities (Vondaloft)

A innovative, modern website design is required for a new startup called Vondaloft. Vondaloft will be an online marketplace for searching for and booking community facilities, such as schools facilities (sports grounds, halls, classrooms etc.), churches, hospitals and other community facilities.

The attached brief has been created to provide guidance on the structure and content required.

The web design shall feature a modern, innovative but user friendly interface similar style to other web start up pages:
www.hirewendle.co.uk
www.trundlo.com.au
www.markplinth.com.au

The web design shall be ‘wordpress’ compliant and allow for future functionality to be added and coded (e.g. animations, flash, blogs etc) and content to be editable.

The following brief has been created to provide guidance on the structure and content required.

An existing logo developed for Vondaloft shall be utilised and incorporated in the top left hand cover of the cover landing page (refer to attached logo designs).

Refer to attached 'Website brief' for more details on requirements.
Updates

Project Deadline Extended
Reason: I wish to grant an extension to the deadline to provide designers with more time to submit their designs.

Target Market(s)

VondaLoft will focus on building a customer network of both community facility owners (schools, hospitals, churches) and hirers (non-government organisations, community groups, event management companies, commercial businesses). Members of the general public will also be encouraged to book facilities for private functions.

Industry/Entity Type

Community

Coding

Coded - Design and coding required

Number of Pages Required

5+ page

Font styles to use
Sans Serif

Colors
3176b5
ffffff
85cae6
33a6d7

Requirements
Must have
• The web design shall feature a modern, innovative but user friendly interface similar style to other web start up pages:
• www.hirewendle.co.uk
• www.trundlo.com.au
• www.markplinth.com.au
• The web design shall be ‘wordpress’ compliant and allow for future functionality to be added and coded (e.g. animations, flash, blogs etc) and content to be editable.
• Refer to Project brief for other requirements
Nice to have
• Refer to Project brief
Should not have
• Refer to Project brief

```html
<!DOCTYPE html>
<html lang="en">
<head>
<meta charset="utf-8">
<title>VondaLoft – Book Community Facilities</title>
<link rel="stylesheet" href="https://fonts.googleapis.com/css2?family=Montserrat:wght@400;500;600;700;800&family=Open+Sans:wght@400;600;700&display=swap">
<style>
:root{
  --blue:#3176b5;
  --blue-deep:#2a64a8;
  --navy:#1f3f73;
  --sky:#85cae6;
  --cyan:#33a6d7;
  --ink:#2b2f36;
  --text:#5d6470;
  --muted:#9aa1ab;
  --line:#e3e7ec;
  --grey-bg:#eef0f2;
  --white:#ffffff;
  --red:#e8483b;
  --teal:#2fc0ad;
  --amber:#f5a623;
  --dark:#15181d;
}
*{box-sizing:border-box;margin:0;padding:0}
html,body{width:1200px;height:4557px;overflow:hidden}
body{font-family:"Open Sans",Arial,sans-serif;color:var(--text);background:var(--white);font-size:13px;line-height:1.6}
h1,h2,h3,h4,.nav a,.btn{font-family:"Montserrat",Arial,sans-serif}
.wrap{width:880px;margin:0 auto;position:relative;height:100%}
section,header,footer{position:relative;overflow:hidden}
.btn{display:inline-block;background:var(--blue);color:var(--white);font-size:13px;font-weight:600;padding:11px 34px;border-radius:2px;text-decoration:none}
.sec-title{text-align:center;font-weight:700;color:var(--blue);font-size:31px;letter-spacing:.5px;line-height:1.2}
.sec-sub{text-align:center;font-family:"Montserrat",sans-serif;font-size:22px;color:var(--ink);letter-spacing:1px;margin-top:4px}

/* top bar */
.topbar{height:30px;background:var(--blue-deep);color:#dce9f7;font-size:11px}
.topbar .wrap{display:flex;align-items:center;justify-content:space-between}
.topbar .contact span{margin-right:20px}
.social{display:flex;gap:8px}
.social i{display:block;width:12px;height:12px;border-radius:50%;background:#cfe0f3}

/* nav */
.navbar{height:62px;background:var(--white);box-shadow:0 2px 6px rgba(0,0,0,.05);z-index:2}
.navbar .wrap{display:flex;align-items:center;justify-content:space-between}
.brand{display:flex;align-items:center;gap:10px;font-family:"Montserrat",sans-serif;font-weight:700;font-size:27px;color:var(--navy)}
.brand i{width:22px;height:22px;border-radius:50%;background:var(--blue);display:block}
.nav{display:flex;gap:22px;align-items:center}
.nav a{font-size:12px;color:var(--ink);text-decoration:none;font-weight:500}
.nav a.active{color:var(--blue);border-bottom:2px solid var(--blue);padding-bottom:3px}

/* hero */
.hero{height:516px;background:linear-gradient(90deg,#f4f6f8 0%,#eef1f4 35%,#dfe5ea 100%)}
.hero-photo{position:absolute;left:390px;top:0;width:810px;height:516px;background:linear-gradient(100deg,rgba(244,246,248,0) 0%,#cfd6dc 30%,#b9c3cc 60%,#8e9aa5 100%)}
.hero-copy{position:absolute;left:182px;top:130px}
.hero-copy h1{font-size:46px;font-weight:800;line-height:1.12;color:var(--navy);letter-spacing:1px}
.hero-copy h1 .hl{color:var(--blue)}
.hero-copy p{font-family:"Montserrat",sans-serif;font-size:22px;color:var(--ink);margin:6px 0 26px;line-height:1.3}

/* about */
.about{height:517px;background:var(--white)}
.about-copy{position:absolute;left:0;top:95px;width:390px}
.about-copy h4{font-size:15px;color:var(--ink);font-weight:700;letter-spacing:.5px}
.about-copy h2{font-size:27px;color:var(--blue);font-weight:800;letter-spacing:1px;margin-bottom:16px}
.about-copy p{font-size:12px;margin-bottom:10px;color:var(--text)}
.about-copy .btn{margin-top:14px}
.about-photo{position:absolute;left:488px;top:62px;width:304px;height:310px;background:linear-gradient(160deg,#c6ccd3,#7b8792 60%,#4e5a66)}

/* how */
.how{height:501px;background:linear-gradient(180deg,#e4e6e9,#f4f5f6 60%,#eceef0)}
.how .sec-title{padding-top:52px}
.how .sec-sub{color:#666}
.how-dash{width:40px;height:3px;background:var(--blue);margin:14px auto 0}
.steps{position:absolute;left:0;top:218px;width:880px;height:240px}
.steps .track{position:absolute;left:-10px;right:-10px;top:75px;height:8px;background:#cfd3d8;border-radius:4px}
.step{position:absolute;top:0;width:170px;text-align:center}
.step svg{display:block;margin:0 auto}
.step .dot{width:8px;height:8px;background:var(--blue);border-radius:50%;margin:8px auto 12px}
.step p{font-size:11px;line-height:1.5;color:var(--text)}

/* benefits */
.benefits{height:532px;background:var(--white)}
.benefits-photo{position:absolute;left:0;top:0;width:593px;height:532px;background:linear-gradient(150deg,#e9ecef,#b8c0c8 50%,#6c7782)}
.benefits-copy{position:absolute;left:628px;top:48px;width:500px}
.benefits-copy h2{font-size:31px;font-weight:800;color:var(--blue);line-height:1.15}
.benefits-copy .lead{font-family:"Montserrat",sans-serif;font-size:18px;color:var(--ink);line-height:1.4;margin-bottom:20px}
.benefits-copy .lead b{color:var(--blue);font-weight:800;border-bottom:2px solid var(--blue)}
.benefit{display:flex;gap:14px;align-items:flex-start;margin-bottom:16px;font-size:12px;color:var(--ink)}
.benefit svg{flex:none}
.sublist{margin:-6px 0 0 48px;font-size:11px;color:var(--ink)}
.sublist li{margin-bottom:2px}

/* services */
.services{height:547px;background:linear-gradient(180deg,#f7f8f9,#eceef0)}
.services .sec-title{padding-top:52px}
.services .sec-sub{font-size:19px}
.cards{position:absolute;top:198px;left:0;width:880px;display:flex;gap:13px}
.card{flex:1;height:222px;background:var(--white);box-shadow:0 3px 10px rgba(0,0,0,.07);padding:22px 18px}
.card .ico{width:72px;height:60px;border-radius:6px;margin-bottom:18px}
.card h3{font-size:14px;color:var(--ink);font-weight:600;line-height:1.3;margin-bottom:8px}
.card p{font-size:10.5px;line-height:1.5}
.services .btn{position:absolute;left:370px;top:458px;padding:11px 46px}

/* packages */
.packages{height:608px;background:var(--white)}
.packages .sec-title{padding-top:60px}
.packages .sec-sub{font-size:20px}
.plans{position:absolute;top:192px;left:90px;width:700px;display:flex;gap:30px}
.plan{flex:1;height:360px;position:relative;color:var(--white);padding-top:36px;text-align:center}
.plan .badge{position:absolute;left:-12px;top:-16px;width:52px;height:52px;border-radius:50%;background:#f3c7a4}
.plan h3{font-size:19px;font-weight:700;letter-spacing:1px;margin-bottom:10px}
.plan .price{background:var(--amber);font-family:"Montserrat",sans-serif;font-weight:700;font-size:24px;padding:8px 0}
.plan .price small{font-size:12px;font-weight:600}
.plan ul{list-style:none;text-align:left;padding:18px 20px 0;font-size:10.5px;line-height:1.4}
.plan li{display:flex;gap:8px;margin-bottom:9px}
.plan li::before{content:"";flex:none;width:5px;height:5px;background:var(--white);border-radius:50%;margin-top:5px}
.plan .buy{position:absolute;left:50%;bottom:24px;transform:translateX(-50%);background:var(--white);font-family:"Montserrat",sans-serif;font-size:12px;font-weight:600;padding:9px 28px;white-space:nowrap}
.basic{background:#2b79c2}.basic .buy{color:#2b79c2}
.standard{background:var(--red)}.standard .buy{color:var(--red)}
.premium{background:var(--teal)}.premium .buy{color:var(--teal)}

/* faq */
.faq{height:350px;background:var(--grey-bg)}
.faq .sec-title{padding-top:36px}
.faq-cols{position:absolute;top:112px;left:90px;width:700px;display:flex;gap:20px}
.faq-col{flex:1}
.q{background:var(--white);font-size:10.5px;color:var(--ink);padding:7px 30px 7px 12px;margin-bottom:6px;position:relative;line-height:1.4}
.q::after{content:"+";position:absolute;right:12px;top:6px;color:var(--blue);font-weight:700}
.q.open{background:var(--blue);color:var(--white);font-weight:600}
.q.open::after{content:"–";color:var(--white)}
.answer{background:var(--white);font-size:10.5px;padding:10px 12px;margin:-6px 0 6px;line-height:1.5;border:1px solid var(--blue)}
.answer p+p{margin-top:6px}

/* news */
.news{height:517px;background:var(--white)}
.news .sec-title{padding-top:56px}
.news .sec-sub{font-size:22px}
.posts{position:absolute;top:158px;left:90px;width:702px;display:flex;gap:10px}
.post{flex:1}
.post .thumb{height:158px}
.post .date{font-family:"Montserrat",sans-serif;color:var(--blue);font-size:12px;margin-top:16px}
.post .date b{font-size:24px;font-weight:600;margin-right:4px}
.post h4{font-size:12px;color:var(--ink);font-weight:600;margin:6px 0 6px}
.post .by{font-size:10px;color:var(--muted);border-top:1px solid var(--line);padding-top:6px}
.post p{font-size:10.5px;line-height:1.5;margin:6px 0}
.post .more{font-size:10.5px;font-weight:700;color:var(--ink)}

/* footer */
.footer{height:350px;background:var(--dark);color:#aab0b8}
.footer .brand{position:absolute;left:50%;top:64px;transform:translateX(-50%);color:var(--white);font-size:40px}
.footer .brand i{width:30px;height:30px;background:var(--white)}
.fcols{position:absolute;top:150px;left:0;width:880px;display:flex;gap:26px}
.fcol h4{color:var(--white);font-size:13px;font-weight:700;margin-bottom:12px}
.fcol p,.fcol li{font-size:10.5px;line-height:1.6}
.fcol ul{list-style:none}
.fcol li::before{content:"›";color:var(--blue);margin-right:6px}
.fcol .sign{display:flex;margin-top:14px}
.fcol .sign span{flex:1;background:var(--white);color:var(--muted);font-size:10px;padding:8px 10px}
.fcol .sign b{width:32px;background:var(--blue);display:flex;align-items:center;justify-content:center}
.bottombar{height:27px;background:var(--blue-deep);color:#dce9f7;font-size:10px}
.bottombar .wrap{display:flex;align-items:center}
</style>
</head>
<body>

<header class="topbar">
  <div class="wrap">
    <div class="contact"><span>Phone: 041 555 0172</span><span>Email: info@vondaloft.com</span></div>
    <div class="social"><i></i><i></i><i></i><i></i><i></i><i></i></div>
  </div>
</header>

<header class="navbar">
  <div class="wrap">
    <div class="brand"><i></i>VondaLoft</div>
    <nav class="nav">
      <a class="active">Home</a><a>About us</a><a>How it work?</a><a>Services</a><a>Packages</a><a>Why Us?</a><a>News</a><a>FAQ</a><a>Contact us</a>
      <svg width="14" height="14" viewBox="0 0 14 14"><circle cx="6" cy="6" r="4.5" fill="none" stroke="#2b2f36" stroke-width="1.8"/><line x1="9.3" y1="9.3" x2="13" y2="13" stroke="#2b2f36" stroke-width="1.8"/></svg>
    </nav>
  </div>
</header>

<section class="hero">
  <div class="hero-photo" role="img" aria-label="Two smiling colleagues working together at a laptop in a bright office"></div>
  <div class="hero-copy">
    <h1><span class="hl">UTILISING</span><br>YOUR <span class="hl">FACILITY</span><br>TO CREATE</h1>
    <p>value for your organisation and<br>the community.</p>
    <a class="btn">Read More</a>
  </div>
</section>

<section class="about">
  <div class="wrap">
    <div class="about-copy">
      <h4>ABOUT US</h4>
      <h2>VONDALOFT</h2>
      <p>The Vondaloft online platform is a convenient and highly functional marketplace for searching and booking community facilities (schools, churches, health care facilities).</p>
      <p>Vondaloft is a start up formed recently by a pair of community-minded co-founders, MK and LR.</p>
      <p>MK and LR both have an interest and/or experience in Project Management, Property Management, Conference and Event Management and Educational Services which underpins this start up business.</p>
      <a class="btn">Read More</a>
    </div>
    <div class="about-photo" role="img" aria-label="Team members joining hands in a circle, seen from above"></div>
  </div>
</section>

<section class="how">
  <div class="wrap">
    <h2 class="sec-title">HOW DOES IT THE <span>BOOKINGS</span></h2>
    <p class="sec-sub">PROCESS WORK?</p>
    <div class="how-dash"></div>
    <div class="steps">
      <div class="track"></div>
      <div class="step" style="left:7px">
        <svg width="150" height="160" viewBox="0 0 150 160"><polygon points="75,2 143,41 143,119 75,158 7,119 7,41" fill="#fff"/><polygon points="75,18 129,49 129,111 75,142 21,111 21,49" fill="#2a64a8"/><circle cx="75" cy="80" r="24" fill="#fff"/><path d="M75 80 L75 56 A24 24 0 0 1 99 80 Z" fill="#85cae6"/></svg>
        <div class="dot"></div>
        <p>Client/hirer looks for advertised space / facility via Vondaloft online platform and makes application</p>
      </div>
      <div class="step" style="left:245px">
        <svg width="150" height="160" viewBox="0 0 150 160"><polygon points="75,2 143,41 143,119 75,158 7,119 7,41" fill="#fff"/><polygon points="75,18 129,49 129,111 75,142 21,111 21,49" fill="#2a64a8"/><rect x="49" y="62" width="52" height="36" fill="#fff"/><polyline points="49,62 75,84 101,62" fill="none" stroke="#2a64a8" stroke-width="3"/></svg>
        <div class="dot"></div>
        <p>Application evaluated by Vondaloft based on guidelines and criteria agreed with facility (licence, insurance)</p>
      </div>
      <div class="step" style="left:470px">
        <svg width="150" height="160" viewBox="0 0 150 160"><polygon points="75,2 143,41 143,119 75,158 7,119 7,41" fill="#fff"/><polygon points="75,18 129,49 129,111 75,142 21,111 21,49" fill="#2a64a8"/><rect x="52" y="52" width="46" height="56" fill="#fff"/><rect x="59" y="62" width="32" height="3" fill="#2a64a8"/><rect x="59" y="71" width="32" height="3" fill="#2a64a8"/><rect x="59" y="80" width="22" height="3" fill="#2a64a8"/><rect x="59" y="92" width="32" height="8" fill="#85cae6"/></svg>
        <div class="dot"></div>
        <p>Booking of facility made via Vondaloft online bookings platform</p>
      </div>
      <div class="step" style="left:700px">
        <svg width="150" height="160" viewBox="0 0 150 160"><polygon points="75,2 143,41 143,119 75,158 7,119 7,41" fill="#fff"/><polygon points="75,18 129,49 129,111 75,142 21,111 21,49" fill="#2a64a8"/><rect x="54" y="52" width="42" height="56" fill="#fff"/><circle cx="62" cy="64" r="3" fill="#2a64a8"/><rect x="69" y="62" width="20" height="3" fill="#2a64a8"/><circle cx="62" cy="78" r="3" fill="#2a64a8"/><rect x="69" y="76" width="20" height="3" fill="#2a64a8"/><circle cx="62" cy="92" r="3" fill="#2a64a8"/><rect x="69" y="90" width="20" height="3" fill="#2a64a8"/></svg>
        <div class="dot"></div>
        <p>Invoice generated and payment received prior to hire of facility</p>
      </div>
    </div>
  </div>
</section>

<section class="benefits">
  <div class="benefits-photo" role="img" aria-label="Business team gathered around a laptop in a meeting room"></div>
  <div class="benefits-copy">
    <h2>WHAT ARE SOME OF THE</h2>
    <p class="lead">key benefits of <b>SIGNING UP</b> with<br>VondaLoft?</p>
    <div class="benefit"><svg width="30" height="30" viewBox="0 0 30 30"><circle cx="15" cy="15" r="15" fill="#3176b5"/><polyline points="9,15 13,19 21,11" fill="none" stroke="#fff" stroke-width="2.5"/></svg><span>Use of existing, underutilised facilities</span></div>
    <div class="benefit"><svg width="30" height="30" viewBox="0 0 30 30"><circle cx="15" cy="15" r="15" fill="#3176b5"/><polyline points="9,15 13,19 21,11" fill="none" stroke="#fff" stroke-width="2.5"/></svg><span>Reduction in administrative time and cost</span></div>
    <div class="benefit"><svg width="30" height="30" viewBox="0 0 30 30"><circle cx="15" cy="15" r="15" fill="#3176b5"/><polyline points="9,15 13,19 21,11" fill="none" stroke="#fff" stroke-width="2.5"/></svg><span>Unregulated revenue stream; low setup fee</span></div>
    <div class="benefit"><svg width="30" height="30" viewBox="0 0 30 30"><circle cx="15" cy="15" r="15" fill="#3176b5"/><polyline points="9,15 13,19 21,11" fill="none" stroke="#fff" stroke-width="2.5"/></svg><span>Managed via a simple, proven and transparent online<br>bookings system</span></div>
    <div class="benefit"><svg width="30" height="30" viewBox="0 0 30 30"><circle cx="15" cy="15" r="15" fill="#3176b5"/><polyline points="9,15 13,19 21,11" fill="none" stroke="#fff" stroke-width="2.5"/></svg><span>Potential for developing marketing and promotional<br>opportunities and establishing commercial relationships</span></div>
    <ul class="sublist"><li>Sporting</li><li>Cultural</li><li>Business/Corporate</li></ul>
  </div>
</section>

<section class="services">
  <div class="wrap">
    <h2 class="sec-title">SERVICES PROVIDED</h2>
    <p class="sec-sub">BY VONDALOFT</p>
    <div class="cards">
      <div class="card"><div class="ico" role="img" aria-label="Colourful ring icon for marketing" style="background:linear-gradient(135deg,#f2b233,#e8483b 50%,#33a6d7)"></div><h3>Marketing and Promotion of your Facility</h3><p>Maintenance and promotion of your custom-made website.</p></div>
      <div class="card"><div class="ico" role="img" aria-label="Calendar icon for bookings" style="background:linear-gradient(135deg,#f7c8b8,#e8483b)"></div><h3>Administer bookings and enquiries</h3><p>All enquiries dealt with via e-mail / telephone from Monday to Friday (9.00am to 5pm)</p></div>
      <div class="card"><div class="ico" role="img" aria-label="Connected network icon" style="background:linear-gradient(135deg,#85cae6,#3176b5)"></div><h3>Administer bookings and enquiries</h3><p>Make changes due to booking cancellations or unforeseen events such as bad weather.</p></div>
      <div class="card"><div class="ico" role="img" aria-label="Hand holding coin icon for payments" style="background:linear-gradient(135deg,#fbd46b,#f5a623)"></div><h3>Invoices and Payment collection</h3><p>Invoices will be raised by Vondaloft on a monthly basis in advance.</p></div>
    </div>
    <a class="btn">View More</a>
  </div>
</section>

<section class="packages">
  <div class="wrap">
    <h2 class="sec-title">SUMMARY OF SUBSCRIPTION PACKAGES</h2>
    <p class="sec-sub">FOR FACILITY OWNERS</p>
    <div class="plans">
      <div class="plan basic"><div class="badge" role="img" aria-label="Rocket illustration"></div><h3>BASIC</h3><div class="price">$15/ <small>MONTHLY</small></div>
        <ul><li>Hosting of facility bookings page on Vondaloft website</li><li>Training and Set-up of Software System</li><li>Maintenance and Support of system during term of use</li></ul>
        <span class="buy">Purchase Now</span></div>
      <div class="plan standard"><div class="badge" role="img" aria-label="Rocket illustration"></div><h3>STANDARD</h3><div class="price">$69/ <small>MONTHLY</small></div>
        <ul><li>Hosting, training, set-up and maintenance of software system (as per Basic)</li><li>Marketing of facility to external hirers</li><li>Additional Admin and support</li></ul>
        <span class="buy">Purchase Now</span></div>
      <div class="plan premium"><div class="badge" role="img" aria-label="Rocket illustration"></div><h3>PREMIUM</h3><div class="price">$30/ <small>MONTHLY</small></div>
        <ul><li>Hosting, set-up, maintenance and admin support of software system</li><li>Marketing of facility to external hirers</li><li>On-site supervision of activities</li><li>Accreditation and Event Manager client</li></ul>
        <span class="buy">Purchase Now</span></div>
    </div>
  </div>
</section>

<section class="faq">
  <div class="wrap">
    <h2 class="sec-title">FREQUENTLY ASKED QUESTIONS</h2>
    <div class="faq-cols">
      <div class="faq-col">
        <div class="q">01 How much does it cost a facility to work with VondaLoft?</div>
        <div class="q open">02 Who is responsible for site supervision/security during facility lettings?</div>
        <div class="answer">
          <p>The hirer will be encouraged to arrange for supervision of the facility during the letting period.</p>
          <p>The facility (although not obliged) is welcome to arrange a resource to supervise during the letting period. This resource may be charged as an additional cost to the hirer through your agreement.</p>
        </div>
      </div>
      <div class="faq-col">
        <div class="q">04 How is insurance dealt with?</div>
        <div class="q">05 What if we require the facilities for our own events or purposes?</div>
        <div class="q">06 Who is responsible for site supervision/security during facility lettings?</div>
        <div class="q">07 What if we already derive an existing income from facility lettings?</div>
      </div>
    </div>
  </div>
</section>

<section class="news">
  <div class="wrap">
    <h2 class="sec-title">LATEST NEWS</h2>
    <p class="sec-sub">LOREM IPSUM IS SIMPLY DUMMY</p>
    <div class="posts">
      <article class="post"><div class="thumb" role="img" aria-label="Team celebrating with raised hands" style="background:linear-gradient(140deg,#d9dde2,#7d8994)"></div>
        <div class="date"><b>15</b>- Jun . 2017</div><h4>10 Tips for best keyword</h4><div class="by">Posted by : Admin</div>
        <p>Lorem ipsum is simply dummy text of the printing and typesetting industry. Lorem ipsum has been the industry.</p><span class="more">Read More</span></article>
      <article class="post"><div class="thumb" role="img" aria-label="Colleagues talking at a conference table" style="background:linear-gradient(140deg,#cfd5db,#6e7a86)"></div>
        <div class="date"><b>31</b>- Jun . 2017</div><h4>10 Tips for best keyword</h4><div class="by">Posted by : Admin</div>
        <p>Lorem ipsum is simply dummy text of the printing and typesetting industry. Lorem ipsum has been the industry.</p><span class="more">Read More</span></article>
      <article class="post"><div class="thumb" role="img" aria-label="Business people in a meeting with laptops" style="background:linear-gradient(140deg,#e2e5e8,#8a95a0)"></div>
        <div class="date"><b>25</b>- Jun . 2017</div><h4>10 Tips for best keyword</h4><div class="by">Posted by : Admin</div>
        <p>Lorem ipsum is simply dummy text of the printing and typesetting industry. Lorem ipsum has been the industry.</p><span class="more">Read More</span></article>
    </div>
  </div>
</section>

<footer class="footer">
  <div class="wrap">
    <div class="brand"><i></i>VondaLoft</div>
    <div class="fcols">
      <div class="fcol" style="width:210px"><h4>ABOUT US</h4><p>The Vondaloft online platform is a convenient and highly functional marketplace for searching and booking community facilities (schools, churches, health care facilities). Vondaloft is a start up formed recently by a pair of community-minded co-founders, MK and LR.</p></div>
      <div class="fcol" style="width:120px"><h4>LINKS</h4><ul><li>HOME</li><li>HOW IT WORK</li><li>SERVICES</li><li>BLOG</li><li>CONTACT</li></ul></div>
      <div class="fcol" style="width:220px"><h4>CONTACT US</h4><p>Lorem ipsum is simply dummy text of the printing and typesetting industry.</p><p style="margin-top:8px"><b style="color:#fff">Address:</b> PO Box 4182,<br>Ferncastle VIC 3912<br><b style="color:#fff">Email:</b> info@vondaloft.com<br><b style="color:#fff">Phone:</b> 03 5550 1190</p></div>
      <div class="fcol" style="width:230px"><h4>NEWSLETTERS</h4><p>Lorem ipsum is simply dummy text of the printing and typesetting industry. Lorem ipsum has been the industry.</p>
        <div class="sign"><span>Your Email Address</span><b><svg width="14" height="14" viewBox="0 0 14 14"><polygon points="1,7 13,1 9,13 7,8" fill="#fff"/></svg></b></div></div>
    </div>
  </div>
</footer>
<div class="bottombar"><div class="wrap">Copyright © 2017 VondaLoft . All Rights Reserved.</div></div>

</body>
</html>
```